Design Card that Captures Life's Moments

Thinking black and white design with maybe some accent colors. Open to others too. Looking for bold and modern to accompany new logo design. For the side without my info, would have tagline of "Capturing Life's Moments" with either logo or website petravossimaging.com. I want the tagline to dominate and be the main focus of that side.

Target Market(s)

Something that can appeal to people who might be interested in family/kids, business, sports, commercial, or birth/newborn photography.

Industry/Entity Type

Professional Photography

Contact Information for Business Card

Font styles to use
Sans Serif
Script
Other font styles liked:
• Go with Logo, but the tagline could be script that popped.

Requirements
Must have
• See details above! Wow factor! Make someone pick my card up and take it home or at least to look at it further.
• Tagline: Capturing Life's Moments (Main text on side without name)
• INFO:
• Petra Voss-Hale - Photographer
• 555-318-0462 - Cell and for SMS
• www.petravossimaging.com - Website (maybe on side with tagline?)
• petra@petrastudioframes.com - Email
Nice to have
• JUST AN IDEA... I would like to see Capturing Life's Moment really take over most of one side of the card. Think greeting card. Where you can't miss it. It is in your face, but nice and elegant. Maybe cursive, but could work with other font. Instead of logo on tagline side, just have petravossimaging.com in smaller text along one of the edges.
Should not have
• Too simple I could of created it, like with only my logo and some typed text.

```html
<!DOCTYPE html>
<html lang="en">
<head>
<meta charset="utf-8">
<title>Petra Voss Photography – Business Card</title>
<link rel="stylesheet" href="https://fonts.googleapis.com/css2?family=Montserrat:wght@300;600;700&family=Open+Sans:wght@600&display=swap">
<style>
  :root {
    --backdrop: #2a2a2a;
    --card: #ffffff;
    --ink: #111111;
    --muted: #444444;
    --rule: #1a1a1a;
  }
  * { margin: 0; padding: 0; box-sizing: border-box; }
  html, body {
    width: 1200px;
    height: 900px;
    overflow: hidden;
    background: var(--backdrop);
  }
  .canvas {
    position: relative;
    width: 1200px;
    height: 900px;
  }
  .card {
    position: absolute;
    width: 520px;
    height: 298px;
    background: var(--card);
    border-radius: 22px;
    color: var(--ink);
    overflow: hidden;
  }
  .card--front { left: 70px; top: 150px; }
  .card--back  { left: 610px; top: 452px; }

  .wordmark {
    font-family: "Montserrat", sans-serif;
    font-weight: 300;
    color: var(--ink);
    white-space: nowrap;
  }

  /* Front: tagline leads */
  .card--front .wordmark {
    position: absolute;
    left: 0; right: 0;
    top: 48px;
    text-align: center;
    font-size: 20px;
    letter-spacing: 0.5px;
  }
  .tagline {
    position: absolute;
    left: 0; right: 0;
    top: 96px;
    text-align: center;
    font-family: "Montserrat", sans-serif;
    font-weight: 700;
    font-size: 38px;
    line-height: 46px;
    letter-spacing: 2px;
    text-transform: uppercase;
  }
  .website {
    position: absolute;
    left: 0; right: 0;
    bottom: 24px;
    text-align: center;
    font-family: "Montserrat", sans-serif;
    font-weight: 600;
    font-size: 12px;
    letter-spacing: 1.6px;
    color: var(--muted);
  }

  /* Back: details */
  .card--back .wordmark {
    position: absolute;
    right: 30px;
    top: 34px;
    font-size: 24px;
  }
  .person {
    position: absolute;
    right: 30px;
    top: 72px;
    text-align: right;
    font-family: "Open Sans", sans-serif;
    font-weight: 600;
    font-size: 13px;
    letter-spacing: 0.4px;
    color: var(--muted);
  }
  .contact {
    position: absolute;
    left: 30px;
    bottom: 26px;
    font-family: "Open Sans", sans-serif;
    font-weight: 600;
    font-size: 15px;
    line-height: 21px;
    list-style: none;
  }
  .contact li { display: flex; align-items: center; gap: 7px; }
  .contact svg { width: 11px; height: 11px; flex: none; }
  .contact__rule {
    position: absolute;
    left: 150px;
    right: 0;
    bottom: 72px;
    height: 1.5px;
    background: var(--rule);
  }
</style>
</head>
<body>
<main class="canvas">
  <section class="card card--front" aria-label="Card front">
    <p class="wordmark">Petra Voss Photography</p>
    <p class="tagline">Capturing<br>Life's Moments</p>
    <p class="website">petravossimaging.com</p>
  </section>

  <section class="card card--back" aria-label="Card back">
    <p class="wordmark">Petra Voss Photography</p>
    <p class="person">Petra Voss-Hale · Photographer</p>
    <div class="contact__rule"></div>
    <ul class="contact">
      <li>Harlow Bay, ME</li>
      <li>
        <svg viewBox="0 0 12 12" aria-hidden="true"><path d="M2.5 1h2l1 2.6-1.3 1a6 6 0 0 0 3.2 3.2l1-1.3L11 7.5v2a1.3 1.3 0 0 1-1.4 1.3A9 9 0 0 1 1.2 2.4 1.3 1.3 0 0 1 2.5 1z" fill="currentColor"/></svg>
        555-318-0462
      </li>
      <li>
        <svg viewBox="0 0 12 12" aria-hidden="true"><rect x="1" y="2.5" width="10" height="7" rx="1" fill="none" stroke="currentColor" stroke-width="1.3"/><path d="M1.5 3l4.5 3.5L10.5 3" fill="none" stroke="currentColor" stroke-width="1.3"/></svg>
        petra@petrastudioframes.com
      </li>
    </ul>
  </section>
</main>
</body>
</html>
```